Mediterranean restaurant menu with psd

i will need this project done by today if possible , 1st page cover 2-3-4menu , 5th page is just blank. i attached a menu that someone made for the restaurant which i really like. you can use the menu information inside those pictures such as the categories , items, decscription , name etc . psd files will be needed thank you

Industry/Entity Type

Restaurant

Requirements
Must have
• 4 pages
• psd file
Nice to have
• something that looks like the uploaded pictures

```html
<!DOCTYPE html>
<html lang="fr">
<head>
<meta charset="utf-8">
<title>Restaurant &amp; Café – Menu</title>
<link href="https://fonts.googleapis.com/css2?family=Old+Standard+TT:wght@400;700&family=Lato:ital,wght@0,400;1,400&display=swap" rel="stylesheet">
<style>
:root{
  --canvas:#ffffff;
  --cream:#efe7d6;
  --cream-light:#f6f0e4;
  --wine:#7e1717;
  --red:#c22a22;
  --rule:#9b4a3f;
  --ink:#5a1010;
  --bar:#3a2a22;
  --wave:#cfe3ee;
}
*{margin:0;padding:0;box-sizing:border-box}
html,body{width:1200px;height:1123px;overflow:hidden;background:var(--canvas)}
body{position:relative;font-family:"Old Standard TT",serif;color:var(--wine)}
.page{position:absolute;background:linear-gradient(180deg,var(--cream-light),var(--cream));overflow:hidden}
.photo{position:absolute}
.snap{position:absolute;border:4px solid #fff;box-shadow:0 2px 6px rgba(0,0,0,.35)}
.wave{position:absolute;left:0;width:100%}

/* cover */
.cover{left:0;top:0;width:398px;height:561px}
.cover-top{left:0;top:0;width:398px;height:175px;background:radial-gradient(ellipse at 30% 50%,#a8452c,#5a2616 60%,#2a160e)}
.cover-grill{left:0;top:330px;width:398px;height:200px;background:radial-gradient(ellipse at 45% 40%,#f49a2a,#b8481a 35%,#3b1e12 75%,#1a0d08)}
.cover-title{position:absolute;left:130px;top:180px;width:230px;text-align:center;z-index:2}
.cover-title .kicker{font-size:17px;color:var(--red);font-variant:small-caps;letter-spacing:1px;transform:rotate(-6deg);display:block;margin-bottom:14px}
.cover-title .word{font-size:30px;font-weight:700;color:var(--red);font-variant:small-caps;letter-spacing:2px}
.cover-title .rule{height:2px;background:var(--red);margin:6px 20px}
.logo-name{position:absolute;left:12px;top:290px;font-size:30px;line-height:36px;color:#2a1a14;z-index:3}
.cover-bar{position:absolute;left:0;bottom:0;width:398px;height:30px;background:var(--bar);color:#fff;font-family:"Lato",sans-serif;font-style:italic;font-size:13px;display:flex;justify-content:space-between;align-items:center;padding:0 12px}
.cover-bar .phone{display:flex;align-items:center;gap:5px}

/* spreads */
.spread-left{left:398px;top:0;width:402px;height:561px}
.spread-right{left:800px;top:0;width:400px;height:561px;border-left:1px solid #ddd2bd}
.drinks{left:202px;top:561px;width:398px;height:562px}
.dessert{left:600px;top:561px;width:399px;height:562px;border-left:1px solid #ddd2bd}

.heading{position:absolute;display:flex;align-items:center;justify-content:center;gap:8px;font-weight:700;font-variant:small-caps;color:var(--wine);font-size:16px;line-height:18px;height:18px;white-space:nowrap}
.heading::before,.heading::after{content:"";width:46px;height:2px;background:linear-gradient(90deg,transparent,var(--wine))}
.heading::after{background:linear-gradient(90deg,var(--wine),transparent)}

.col{position:absolute;display:flex;flex-direction:column}
.item{display:flex;justify-content:space-between;align-items:flex-end;font-size:8px;font-weight:700;font-variant:small-caps;line-height:1;border-bottom:1px solid var(--rule);padding:2px 0 1px;color:var(--ink)}
.item small{display:block;font-size:5.5px;line-height:1;font-weight:400;font-style:italic;font-variant:normal;color:#7a4a3a}
.item sup{font-size:5.5px;line-height:0}
.note{position:absolute;font-style:italic;font-weight:700;font-size:10px;line-height:12px;text-align:center;color:#2a1a14}
</style>
</head>
<body>

<!-- Cover -->
<section class="page cover">
  <div class="photo cover-top" role="img" aria-label="Grilled lamb shank close-up"></div>
  <svg class="wave" style="top:140px" width="398" height="60" viewBox="0 0 398 60"><path d="M0 40 C120 0 260 60 398 10 L398 60 L0 60Z" fill="#f6f0e4"/></svg>
  <div class="cover-title">
    <span class="kicker">Restaurant &amp; Café</span>
    <div class="rule"></div>
    <div class="word">Menu</div>
    <div class="rule"></div>
  </div>
  <div class="logo-name">LOGO</div>
  <div class="photo cover-grill" role="img" aria-label="Steaks on a flaming grill"></div>
  <svg class="wave" style="top:320px" width="398" height="50" viewBox="0 0 398 50"><path d="M0 40 C140 0 260 10 398 30 L398 0 L0 0Z" fill="#efe7d6"/><path d="M0 44 C140 4 260 14 398 34" stroke="#fff" stroke-width="3" fill="none" opacity=".7"/></svg>
  <div class="cover-bar">
    <span>4200 rue des Oliviers H2X 3B7</span>
    <span class="phone"><svg width="11" height="11" viewBox="0 0 24 24"><circle cx="12" cy="12" r="11" fill="none" stroke="#fff" stroke-width="2"/><path d="M8 6l2 3-1.5 1.5c.8 1.8 2.2 3.2 4 4L14 13l3 2-1 2.5C11 17 7 13 6.5 8z" fill="#fff"/></svg>514-555-0148</span>
  </div>
</section>

<!-- Spread left: starters, salads, sandwiches -->
<section class="page spread-left">
  <div class="photo" style="left:20px;top:0;width:300px;height:140px;background:radial-gradient(ellipse at 50% 40%,#8a4a26,#4a2412 60%,#e8e2d8 62%,#f3efe8)" role="img" aria-label="Plate of grilled lamb chops"></div>
  <div class="photo" style="left:325px;top:0;width:77px;height:140px;background:linear-gradient(90deg,#d58a3a,#eadfcf)" role="img" aria-label="Grilled vegetables"></div>
  <svg class="wave" style="top:100px" width="402" height="70" viewBox="0 0 402 70"><path d="M0 20 C120 70 280 60 402 30 L402 70 L0 70Z" fill="#f3ece0"/></svg>

  <div class="heading" style="left:0;width:402px;top:170px">Les Entrées</div>
  <div class="col" style="left:45px;top:191px;width:147px">
    <div class="item"><span>Briouates aux<small>fruits de mer</small></span><span>4.<sup>99</sup> $</span></div>
    <div class="item"><span>Crevettes à l'ail</span><span>$</span></div>
    <div class="item"><span>Zaalouk<small>Aubergine, piment, tomate,<br>coriandre, soupçon de cumin</small></span><span>$</span></div>
    <div class="item"><span>Soupe harira</span><span>$</span></div>
  </div>
  <div class="col" style="left:210px;top:191px;width:147px">
    <div class="item"><span>Humus</span><span>$</span></div>
    <div class="item"><span>Calmars<small>à la sauce tomate</small></span><span>$</span></div>
    <div class="item"><span>Ailes de poulet<small>à la sauce douce ou piquante</small></span><span>$</span></div>
    <div class="item"><span>Soupe du jour</span><span>$</span></div>
  </div>

  <div class="heading" style="left:0;width:402px;top:264px">Les salades</div>
  <div class="col" style="left:45px;top:284px;width:147px">
    <div class="item"><span>Salade marocaine</span><span>$</span></div>
    <div class="item"><span>Salade César</span><span>$</span></div>
    <div class="item"><span>Salade de betteraves</span><span>$</span></div>
  </div>
  <div class="col" style="left:210px;top:284px;width:147px">
    <div class="item"><span>Salade grecque</span><span>$</span></div>
    <div class="item"><span>Salade au poulet grillé</span><span>$</span></div>
    <div class="item"><span>Salade du chef</span><span>$</span></div>
  </div>

  <div class="heading" style="left:0;width:402px;top:322px;font-size:17px">Sandwich&amp;burger</div>
  <div class="col" style="left:45px;top:343px;width:147px">
    <div class="item"><span>Sandwich<small>de filet mignon</small></span><span>$</span></div>
    <div class="item"><span>Sandwich<small>de kafta</small></span><span>$</span></div>
  </div>
  <div class="col" style="left:210px;top:343px;width:147px">
    <div class="item"><span>Sandwich<small>de poitrine de poulet</small></span><span>$</span></div>
    <div class="item"><span>Sandwich<small>de merguez</small></span><span>$</span></div>
  </div>

  <svg class="wave" style="top:430px" width="402" height="80" viewBox="0 0 402 80"><path d="M0 50 C140 10 260 70 402 20" stroke="var(--wave)" stroke-width="10" fill="none"/></svg>
  <div class="snap" style="left:30px;top:420px;width:96px;height:90px;transform:rotate(-3deg);background:radial-gradient(circle,#e8743a,#6aa24a 60%,#f2efe8)" role="img" aria-label="Fresh vegetable salad"></div>
  <div class="snap" style="left:140px;top:455px;width:100px;height:88px;background:radial-gradient(circle,#e2a27a,#7a9a5a 60%,#f2efe8)" role="img" aria-label="Shrimp salad"></div>
  <div class="snap" style="left:238px;top:415px;width:112px;height:88px;transform:rotate(-8deg);background:radial-gradient(circle,#9a4a2a,#6a8a4a 60%,#f2efe8)" role="img" aria-label="Grilled chicken salad"></div>
</section>

<!-- Spread right: burgers and mains -->
<section class="page spread-right">
  <div class="photo" style="left:0;top:0;width:400px;height:145px;background:linear-gradient(100deg,#c9762e,#e8b06a 40%,#efd7b8 70%,#f3eadb)" role="img" aria-label="Grilled chicken breast with vegetables"></div>
  <svg class="wave" style="top:105px" width="400" height="70" viewBox="0 0 400 70"><path d="M0 30 C120 60 280 70 400 20 L400 70 L0 70Z" fill="#f3ece0"/></svg>

  <div class="heading" style="left:0;width:400px;top:166px;font-size:17px">Sandwich&amp;burger</div>
  <div class="col" style="left:42px;top:186px;width:148px">
    <div class="item"><span>Hamburger</span><span>$</span></div>
    <div class="item"><span>Burger au poulet</span><span>$</span></div>
    <div class="item"><span>Poutine</span><span>$</span></div>
    <div class="item"><span>Poutine merguez</span><span>$</span></div>
  </div>
  <div class="col" style="left:208px;top:186px;width:148px">
    <div class="item"><span>Cheeseburger</span><span>$</span></div>
    <div class="item"><span>Frites</span><span>$</span></div>
    <div class="item"><span>Poutine poulet</span><span>$</span></div>
    <div class="item"><span>Poutine viande</span><span>$</span></div>
  </div>

  <div class="heading" style="left:0;width:400px;top:236px;font-size:14px">Plats principaux et grillades</div>
  <div class="col" style="left:42px;top:257px;width:148px">
    <div class="item"><span>Assiette de fillet<br>Mignon</span><span>1p &nbsp; $<br>2p &nbsp; $</span></div>
    <div class="item"><span>Assiette de<br>poitrine de poulet</span><span></span></div>
    <div class="item"><span>Assiette de Merguez</span><span>$</span></div>
    <div class="item"><span>Assiette mixte</span><span></span></div>
    <div class="item"><span>Assiette de<br>poulet et crevettes</span><span></span></div>
    <div class="item"><span>Assiette de<br>filet mignon et poulet</span><span>$</span></div>
    <div class="item"><span>Tajine de kefta</span><span>$</span></div>
  </div>
  <div class="col" style="left:208px;top:257px;width:148px">
    <div class="item"><span>Assiette de<br>brochettes de poulet</span><span>$</span></div>
    <div class="item"><span>Assiette de kefta</span><span>$</span></div>
    <div class="item"><span>Assiette de crevettes</span><span>$</span></div>
    <div class="item"><span>Couscous marocain<small>NB: seulement le vendredi</small></span><span>$</span></div>
    <div class="item"><span>Assiette de<br>filet mignon et crevettes</span><span></span></div>
    <div class="item"><span>Tajine de moules</span><span>$</span></div>
    <div class="item"><span>Tajine du jour</span><span>$</span></div>
  </div>
  <div class="note" style="left:0;width:400px;top:380px">Tous les assiettes sont servis avec deux des choix suivants:<br>salade, riz, légumes grillés, frites.</div>

  <svg class="wave" style="top:440px" width="400" height="80" viewBox="0 0 400 80"><path d="M0 40 C140 70 260 10 400 40" stroke="var(--wave)" stroke-width="10" fill="none"/></svg>
  <div class="snap" style="left:18px;top:425px;width:100px;height:90px;transform:rotate(-4deg);background:radial-gradient(circle,#b85a2a,#5a2412 70%)" role="img" aria-label="Grilled kebabs and meat"></div>
  <div class="snap" style="left:125px;top:435px;width:104px;height:85px;background:radial-gradient(ellipse at 50% 35%,#d88a2a,#f3efe8 55%)" role="img" aria-label="Bowl of soup"></div>
  <div class="snap" style="left:240px;top:420px;width:128px;height:95px;background:radial-gradient(circle,#c06a4a,#6a8a3a 70%,#f3efe8)" role="img" aria-label="Sliced grilled meat with garnish"></div>
</section>

<!-- Drinks page -->
<section class="page drinks">
  <div class="photo" style="left:0;top:0;width:398px;height:190px;background:linear-gradient(90deg,#4a6a9a,#c08a5a 35%,#9a4a3a 55%,#4a6a9a 80%,#d8cdbb)" role="img" aria-label="Moroccan mint tea glasses"></div>
  <svg class="wave" style="top:100px" width="398" height="92" viewBox="0 0 398 92"><path d="M0 80 C120 70 280 30 398 10 L398 92 L0 92Z" fill="#f3ece0"/></svg>

  <div class="heading" style="left:0;width:398px;top:195px;font-size:17px">Cafe &amp; The</div>
  <div class="col" style="left:14px;top:216px;width:150px">
    <div class="item"><span>Espresso</span><span>2.<sup>50</sup> $</span></div>
    <div class="item"><span>Double Espresso</span><span>2.<sup>99</sup> $</span></div>
    <div class="item"><span>Café au lait</span><span>3.<sup>50</sup> $</span></div>
    <div class="item"><span>Café mocha</span><span>3.<sup>50</sup> $</span></div>
    <div class="item"><span>Farouza</span><span>4.<sup>00</sup> $</span></div>
    <div class="item"><span>Thé glacé</span><span>3.<sup>00</sup> $</span></div>
    <div class="item"><span>Perlette</span><span>3.<sup>00</sup> $</span></div>
  </div>
  <div class="col" style="left:180px;top:216px;width:150px">
    <div class="item"><span>Chocolat chaud</span><span>3.<sup>00</sup> $</span></div>
    <div class="item"><span>Cappuccino<br>&nbsp;<br>The Marocain</span><span>3.<sup>50</sup> $<br>(G)7.<sup>00</sup> $<br>(M)5.<sup>00</sup> $</span></div>
    <div class="item"><span>Boisson gazeuses</span><span>2.<sup>00</sup> $</span></div>
    <div class="item"><span>Lazira</span><span>4.<sup>00</sup> $</span></div>
    <div class="item"><span>San Vitale</span><span>3.<sup>00</sup> $</span></div>
    <div class="item"><span>Eau</span><span>1.<sup>50</sup> $</span></div>
  </div>

  <div class="heading" style="left:0;width:398px;top:310px;font-size:17px">Jus</div>
  <div class="col" style="left:14px;top:331px;width:150px">
    <div class="item"><span>Jus de pomme</span><span>$</span></div>
    <div class="item"><span>Jus de banane</span><span>$</span></div>
    <div class="item"><span>Smoothie d'avocat</span><span>6.<sup>00</sup> $</span></div>
    <div class="item"><span>Smoothie de fraise</span><span>6.<sup>00</sup> $</span></div>
    <div class="item"><span>Smoothie de mangue</span><span>6.<sup>00</sup> $</span></div>
  </div>
  <div class="col" style="left:180px;top:331px;width:150px">
    <div class="item"><span>Jus d'orange</span><span>4.<sup>00</sup> $</span></div>
    <div class="item"><span>Jus de citron</span><span>3.<sup>50</sup> $</span></div>
    <div class="item"><span>Jus de canneberge</span><span>3.<sup>00</sup> $</span></div>
    <div class="item"><span>Jus d'avocat avec</span><span>6.<sup>00</sup> $</span></div>
    <div class="item"><span>Fruit sec</span><span></span></div>
  </div>

  <svg class="wave" style="top:420px" width="398" height="120" viewBox="0 0 398 120"><path d="M0 90 C140 40 260 110 398 60" stroke="var(--wave)" stroke-width="10" fill="none"/></svg>
  <div class="snap" style="left:12px;top:430px;width:90px;height:88px;background:radial-gradient(circle,#e8dccb,#a07a5a 55%,#6a4a3a)" role="img" aria-label="Cup of café au lait"></div>
  <div class="snap" style="left:105px;top:425px;width:96px;height:100px;transform:rotate(6deg);background:radial-gradient(ellipse at 50% 60%,#fbf8f2,#d8d8d8)" role="img" aria-label="Milkshake with striped straw"></div>
  <div class="snap" style="left:205px;top:428px;width:96px;height:92px;background:radial-gradient(circle,#c89a6a,#7a3a22 55%,#5a3a2a)" role="img" aria-label="Latte art cappuccino"></div>
</section>

<!-- Dessert page -->
<section class="page dessert">
  <div class="photo" style="left:0;top:0;width:399px;height:190px;background:radial-gradient(ellipse at 40% 45%,#f2a232,#f6e2a4 35%,#e8e0d2 60%,#6a9a4a 95%)" role="img" aria-label="Slice of orange sponge cake"></div>
  <svg class="wave" style="top:100px" width="399" height="92" viewBox="0 0 399 92"><path d="M0 85 C140 90 280 50 399 25 L399 92 L0 92Z" fill="#f3ece0"/></svg>
  <svg class="wave" style="top:420px" width="399" height="120" viewBox="0 0 399 120"><path d="M0 60 C140 110 260 40 399 70" stroke="var(--wave)" stroke-width="10" fill="none"/></svg>
</section>

</body>
</html>
```